MIRAGES OVER ZERATHON LP - COVER ART

I need a cover (also formatted to be used for digital release), 4 Pages Booklet inlay Both Sides, a back cover, and a CD image for a pop-rock album called Faded Mirages over Zerathon, qui est Both the name of the album and the artist. Music acts porte sur Such As Copperwave, Tal Merrow, Falcon, K7 and Duskfield. It will be available to download from all major digital distributors, as well as a very limited physical release (Jewel Box - clear tray). Please Note this is a self-produced project. I am looking for a Design That Is Both faithful to the musical identity of the project (mixes are Provided for reference and inspiration) and aussi Provides with a striking, elegant, clever and impactful image. My favorite visual inspirations come from Quorlo ( "Sleeping on Glass"), Teddy Granick (movie posters and papercuts) and Velvet Lattice (Iron Bay and Hollow Signals design titles): a few references are Provided, along with iconic album covers. Rob Tellguard Nightwarden we can be an alternative source of inspiration. I have no specific demand Regarding the actual design. HOWEVER, Meaningful lyrics from the album That Could be used visually include: - Mini Tree Of Life - Lake of fire - Deer - Pied Piper - Roots in the sky - A pyramid mirrored in my eye - Orrimak The Following information must be included inside the 4-page booklet, but not on the front cover. Here are the tracks, aussi to feature on the back cover. Tracks: 1. Mend The Kettle Mirages 2. 3. 4. Copper Fern Panic Before Supper 5. Song For The Ferryman Velden 6. 7. 8. Song Under The Gravel Orrimak 9. Last Thaw Songs by Etienne Voulard Co-Produced by Etienne Voulard & TM Drovetti Engineered, mixed and mastered by TM Drovetti Track 7 Arranged and produced by Gil Voulard / Vocals Recorded by Sam Kettering Tracks 8 engineered and mixed by Sam Kettering Etienne Voulard: Vocals / Grand Piano / Electric & Acoustic Guitars / Keyboards / Strings Arrangement / Ukulele / Tovan Kessler / Brevik Organ / Synth Bass TM Drovetti: Drums / Bass / Bass Ukulele Gil Voulard: Drums / Bass / Piano / Keyboards on Track 7 - Additional Strings Arrangement is Tracks 2 & 4 Owen Brisk: Drums / on Percussion Track 8 Copyright © 2017 EV - all rights reserved must Have: - The project must fit the music and look like what Quorlo et / ou Teddy Granick Would Have done, hAD they beens commissioned  The visual must be touching, poetic with a twist of dry humor - it must have the title of the album on the cover and CD picture (but not twice as the title and the artist name are the same - think concept album). Changes or extensions of the Saami picture can be used for the CD image and insert back cover. Should Not Have: - No literal illustration of Babylon (qui is used metaphorically)

Target Market(s)

Fans of Copperwave, Tal Merrow, Duskfield, Kestle, Falcon, Gravel, TVK ...

Industry/Entity Type

Digital

Font styles to use
Serif
Sans Serif
Decorative
Script

Requirements
Must have
• - The project must fit the music and look like what Quorlo et / ou Teddy Granick Would Have done, HAD They beens commissioned  The visual must be touching, poetic with a twist of dry humor - It must have the title of the album on the cover and CD picture (but not twice as the title and the artist name are the same - think concept album). Changes or extensions of the Saami picture can be used for the CD image and insert back cover.
Should not have
• - No literal illustration of Babylon (qui is used metaphorically)

```html
<!DOCTYPE html>
<html lang="en">
<head>
<meta charset="utf-8">
<title>Mirages over Zerathon — Cover</title>
<link rel="stylesheet" href="https://fonts.googleapis.com/css2?family=Open+Sans:wght@300;700&display=swap">
<style>
  :root {
    --paper: #cde04f;
    --paper-light: #d9ea6c;
    --paper-shade: #b8cc3c;
    --title: #f4eef2;
    --ghost: #bccc47;
    --art-teal: #2fa6cc;
    --art-blue: #3b6fb3;
    --art-deep: #4a4f9e;
    --art-magenta: #e0206f;
    --art-orange: #f0843a;
    --art-yellow: #f6d24a;
  }
  html, body {
    margin: 0;
    padding: 0;
    width: 1200px;
    height: 1200px;
    overflow: hidden;
  }
  .cover {
    position: relative;
    width: 1200px;
    height: 1200px;
    overflow: hidden;
    background:
      radial-gradient(ellipse at 18% 12%, var(--paper-light) 0%, transparent 45%),
      radial-gradient(ellipse at 88% 85%, var(--paper-shade) 0%, transparent 50%),
      linear-gradient(160deg, var(--paper-light) 0%, var(--paper) 50%, var(--paper-shade) 100%);
  }
  .paper-texture {
    position: absolute;
    inset: 0;
    width: 1200px;
    height: 1200px;
    mix-blend-mode: multiply;
    opacity: 0.38;
  }
  .paper-folds {
    position: absolute;
    inset: 0;
    background:
      linear-gradient(90deg, transparent 50.6%, rgba(90,110,0,0.10) 50.8%, rgba(255,255,255,0.10) 51%, transparent 51.2%),
      linear-gradient(0deg, transparent 18.6%, rgba(90,110,0,0.10) 18.8%, rgba(255,255,255,0.10) 19%, transparent 19.2%),
      linear-gradient(0deg, transparent 33.6%, rgba(90,110,0,0.08) 33.8%, transparent 34%),
      linear-gradient(0deg, transparent 67.8%, rgba(90,110,0,0.08) 68%, transparent 68.2%),
      linear-gradient(0deg, transparent 96.4%, rgba(90,110,0,0.08) 96.6%, transparent 96.8%);
  }
  .artwork {
    position: absolute;
    left: 158px;
    top: 136px;
    width: 904px;
    height: 904px;
  }
  .ghost-line {
    position: absolute;
    left: 0;
    width: 1200px;
    top: 1068px;
    margin: 0;
    text-align: center;
    font-family: "Open Sans", sans-serif;
    font-weight: 300;
    font-size: 36px;
    line-height: 56px;
    letter-spacing: 24px;
    text-indent: 24px;
    color: var(--ghost);
    white-space: nowrap;
  }
  .album-title {
    position: absolute;
    left: 0;
    width: 1200px;
    top: 1068px;
    margin: 0;
    text-align: center;
    font-family: "Open Sans", sans-serif;
    font-weight: 700;
    font-size: 40px;
    line-height: 56px;
    letter-spacing: 17px;
    text-indent: 17px;
    color: var(--title);
    white-space: nowrap;
  }
</style>
</head>
<body>
<main class="cover">
  <svg class="paper-texture" viewBox="0 0 1200 1200" aria-hidden="true">
    <filter id="crumple" x="0" y="0" width="100%" height="100%">
      <feTurbulence type="fractalNoise" baseFrequency="0.006 0.009" numOctaves="4" seed="7" result="noise"/>
      <feDiffuseLighting in="noise" lighting-color="#ffffff" surfaceScale="5" result="light">
        <feDistantLight azimuth="225" elevation="52"/>
      </feDiffuseLighting>
    </filter>
    <rect width="1200" height="1200" filter="url(#crumple)"/>
  </svg>
  <div class="paper-folds"></div>

  <svg class="artwork" viewBox="0 0 904 904" role="img" aria-label="Psychedelic thermal-coloured photograph of a hooded figure whose eyes are covered by a blazing streak, set against mountains under an orange sky">
    <defs>
      <clipPath id="disc"><circle cx="452" cy="452" r="452"/></clipPath>
      <linearGradient id="artBase" x1="0" y1="0" x2="1" y2="1">
        <stop offset="0%" stop-color="var(--art-teal)"/>
        <stop offset="50%" stop-color="var(--art-blue)"/>
        <stop offset="100%" stop-color="var(--art-deep)"/>
      </linearGradient>
      <linearGradient id="artSky" x1="0" y1="0" x2="0" y2="1">
        <stop offset="0%" stop-color="var(--art-orange)"/>
        <stop offset="22%" stop-color="var(--art-orange)" stop-opacity="0.85"/>
        <stop offset="34%" stop-color="var(--art-magenta)" stop-opacity="0.55"/>
        <stop offset="46%" stop-color="var(--art-magenta)" stop-opacity="0"/>
      </linearGradient>
      <radialGradient id="artCore" cx="50%" cy="62%" r="45%">
        <stop offset="0%" stop-color="var(--art-magenta)" stop-opacity="0.55"/>
        <stop offset="60%" stop-color="var(--art-deep)" stop-opacity="0.35"/>
        <stop offset="100%" stop-color="var(--art-deep)" stop-opacity="0"/>
      </radialGradient>
      <radialGradient id="artLower" cx="55%" cy="100%" r="45%">
        <stop offset="0%" stop-color="var(--art-magenta)" stop-opacity="0.7"/>
        <stop offset="100%" stop-color="var(--art-magenta)" stop-opacity="0"/>
      </radialGradient>
      <radialGradient id="artBlaze" cx="50%" cy="50%" r="50%">
        <stop offset="0%" stop-color="var(--art-yellow)"/>
        <stop offset="45%" stop-color="var(--art-orange)" stop-opacity="0.9"/>
        <stop offset="75%" stop-color="var(--art-magenta)" stop-opacity="0.5"/>
        <stop offset="100%" stop-color="var(--art-magenta)" stop-opacity="0"/>
      </radialGradient>
      <radialGradient id="artEdgeLeft" cx="5%" cy="50%" r="40%">
        <stop offset="0%" stop-color="var(--art-teal)" stop-opacity="0.8"/>
        <stop offset="100%" stop-color="var(--art-teal)" stop-opacity="0"/>
      </radialGradient>
    </defs>
    <g clip-path="url(#disc)">
      <rect width="904" height="904" fill="url(#artBase)"/>
      <rect width="904" height="904" fill="url(#artEdgeLeft)"/>
      <rect width="904" height="904" fill="url(#artSky)"/>
      <rect width="904" height="904" fill="url(#artCore)"/>
      <rect width="904" height="904" fill="url(#artLower)"/>
      <ellipse cx="470" cy="300" rx="260" ry="105" transform="rotate(-12 470 300)" fill="url(#artBlaze)"/>
    </g>
  </svg>

  <p class="ghost-line" aria-hidden="true">ONCE WANDERING CANYON</p>
  <h1 class="album-title">MIRAGES OVER ZERATHON</h1>
</main>
</body>
</html>
```